Lotuvan Cafe Menu rev.01

Design an elegant menu for Khmer restaurant in Melbourne.

-Size and format can be proposed (not bigger than A3)
-Food and beverages split (separate sides of the menu)
-Sample excel file - Food attached
-Sample Menu Pdf attached (just to get an idea)
-Details shall be reviewed and considered
-Prices in AUD
-Easy to print and clean (format need to to printable)
-Provision for future updates.

If you have any further question please let us know.
Regards,

Dexter

Target Market(s)

Customers win the restaurant

Industry/Entity Type

Hospitality - Restaurant

Colors

Designer to choose colors to be used in the design.

Requirements
Must have
• Authentic touch - clear structure
Nice to have
• Welcome about the restaurant. Complete information - see sample menu

```html
<!DOCTYPE html>
<html lang="en">
<head>
<meta charset="utf-8">
<title>Lotuvan Cafe — Menu</title>
<link rel="stylesheet" href="https://fonts.googleapis.com/css2?family=Saira:wght@500;600&family=Marcellus+SC&family=Open+Sans:wght@400&display=swap">
<style>
  :root {
    --canvas: #ffffff;
    --paper-light: #fbf3e5;
    --paper-dark: #f1e2c8;
    --ink: #1c1c1c;
    --ink-soft: #2e2e2e;
    --maroon: #8e1c22;
    --maroon-soft: #a3383c;
    --shadow: #8d8d8d;
    --bloom: rgba(240, 178, 160, 0.45);
    --bloom-fade: rgba(240, 178, 160, 0);
  }
  * { box-sizing: border-box; margin: 0; padding: 0; }
  html, body { width: 1200px; height: 1200px; overflow: hidden; background: var(--canvas); }
  .canvas { position: relative; width: 1200px; height: 1200px; }

  .page {
    position: absolute; width: 342px; height: 484px;
    background: radial-gradient(ellipse at 55% 45%, var(--paper-light), var(--paper-dark));
    box-shadow: 4px 4px 0 var(--shadow);
    overflow: hidden;
    font-family: "Saira", sans-serif; color: var(--ink);
  }
  .page--tall { height: 488px; }
  .page--cover { left: 58px; top: 108px; }
  .page--starters { left: 432px; top: 108px; }
  .page--mains { left: 817px; top: 108px; }
  .page--salads { left: 207px; top: 640px; }
  .page--notes { left: 616px; top: 640px; }

  .frame { position: absolute; inset: 0; width: 100%; height: 100%; }
  .frame path { fill: none; stroke: var(--ink); stroke-width: 0.9; }

  /* Artwork zones: one soft gradient each */
  .artwork { position: absolute; }
  .artwork--top-right { right: 0; top: 0; width: 170px; height: 180px;
    background: linear-gradient(215deg, var(--bloom), var(--bloom-fade) 70%); }
  .artwork--bottom-left { left: 0; bottom: 0; width: 180px; height: 180px;
    background: linear-gradient(35deg, var(--bloom), var(--bloom-fade) 70%); }
  .artwork--top-left { left: 0; top: 0; width: 200px; height: 160px;
    background: linear-gradient(145deg, var(--bloom), var(--bloom-fade) 70%); }
  .artwork--bottom-right { right: 0; bottom: 0; width: 180px; height: 170px;
    background: linear-gradient(-35deg, var(--bloom), var(--bloom-fade) 70%); }
  .artwork--wreath { left: 20px; top: 20px; width: 300px; height: 440px;
    background: radial-gradient(ellipse at center, var(--bloom) 30%, var(--bloom-fade) 68%); }

  .brand-badge { position: absolute; left: 45px; top: 117px; width: 250px; height: 250px; border-radius: 50%;
    background: #fff;
    display: flex; align-items: center; justify-content: center; }
  .brand-name { font-family: "Saira", sans-serif; font-weight: 600; font-size: 34px; color: var(--ink); letter-spacing: 1px; }

  .section-label { position: absolute; height: 16px; background: var(--maroon); color: #fff;
    font-family: "Marcellus SC", serif; font-size: 11px; line-height: 16px; padding: 0 4px; white-space: nowrap; }
  .section-label--center { text-align: center; }
  .section-label--right { text-align: right; }

  .item { position: absolute; }
  .item-name { font-size: 10.5px; font-weight: 600; line-height: 12px; white-space: nowrap; }
  .item-desc { font-family: "Open Sans", sans-serif; font-size: 5.3px; line-height: 7.2px; color: var(--ink-soft); }
  .item--right { text-align: right; }
  .item--center { text-align: center; }
  .price { display: inline-block; }

  .notes-list { position: absolute; left: 47px; top: 172px; width: 245px;
    font-family: "Open Sans", sans-serif; font-size: 8.6px; line-height: 12.6px; color: var(--ink-soft); list-style: disc; padding-left: 13px; }
  .dietary-key { position: absolute; font-family: "Marcellus SC", serif; font-size: 10px; color: var(--maroon-soft); letter-spacing: .3px; white-space: nowrap; }
</style>
</head>
<body>
<main class="canvas">

  <!-- Cover -->
  <section class="page page--cover">
    <svg class="frame" viewBox="0 0 342 484" aria-hidden="true">
      <path d="M207 20 H20 V167"/><path d="M207 25 H25 V167"/>
      <path d="M173 465 H323 V279"/><path d="M173 460 H318 V279"/>
    </svg>
    <div class="artwork artwork--wreath" role="img" aria-label="Watercolour wreath of pink and peach roses with teal and sage leaves"></div>
    <div class="brand-badge"><span class="brand-name">Lotuvan Cafe</span></div>
  </section>

  <!-- Starters and Khmer breakfast -->
  <section class="page page--starters">
    <div class="artwork artwork--top-right" role="img" aria-label="Watercolour peach and pink roses with teal leaves"></div>
    <div class="artwork artwork--bottom-left" role="img" aria-label="Watercolour pink roses with teal leaves"></div>
    <svg class="frame" viewBox="0 0 342 484" aria-hidden="true">
      <path d="M207 20 H20 V167"/><path d="M207 25 H25 V167"/>
      <path d="M173 465 H323 V279"/><path d="M173 460 H318 V279"/>
    </svg>

    <div class="section-label" style="left:44px;top:53px;width:78px;">TASTY BITES</div>

    <div class="item" style="left:47px;top:81px;width:180px;">
      <div class="item-name">Betel Leaf<span class="price" style="position:absolute;left:142px;">04.50</span></div>
      <div class="item-desc" style="margin-top:3px;width:118px;">A traditional Cambodian appetizer, betel leaf with Asian Pomegranate, prawns, herbs and special Lotuvan sauce with a dust of peanuts or coconut shredded (1 pcs)</div>
    </div>
    <div class="item" style="left:47px;top:135px;width:180px;">
      <div class="item-name">Crispy Sweet Potatoes<span class="price" style="position:absolute;left:145px;">06.00</span></div>
      <div class="item-desc">Fritted finger strips of sweet potatoes served in a bowl</div>
    </div>
    <div class="item" style="left:47px;top:164px;width:180px;">
      <div class="item-name">Spring Rolls<span class="price" style="position:absolute;left:147px;">10.20</span></div>
      <div class="item-desc">Deep fried roll with pork and prawns, vegetable (3 pcs)</div>
    </div>
    <div class="item" style="left:47px;top:192px;width:180px;">
      <div class="item-name">Vegetarian Spring Rolls<span class="price" style="position:absolute;left:150px;">09.00</span></div>
      <div class="item-desc">Deep fired roll, vegetable (3 pcs)</div>
    </div>
    <div class="item" style="left:47px;top:221px;width:180px;">
      <div class="item-name">BBQ Scallop<span class="price" style="position:absolute;left:147px;">10.00</span></div>
      <div class="item-desc">Sea scallop with herbs and special Lotuvan dressing (2 pcs)</div>
    </div>

    <div class="section-label section-label--center" style="left:129px;top:276px;width:168px;">Khmer Breakfast or Lunch</div>

    <div class="item item--right" style="right:53px;top:299px;width:170px;">
      <div class="item-name"><span class="price" style="position:absolute;left:6px;">15.50</span>Kuy Teav Phnom Penh</div>
      <div class="item-desc">"Traditional Cambodian noodle soup, rice and yellow<br>noodles, choice of Pork, Beef or Seafood"</div>
    </div>
    <div class="item item--right" style="right:53px;top:335px;width:170px;">
      <div class="item-name"><span class="price" style="position:absolute;left:9px;">14.50</span>Lot Cha</div>
      <div class="item-desc">Rice drop noodles with Chinese chives, bean sprouts, chicken,<br>beef ham and a dust of special Lotuvan sauce</div>
    </div>
    <div class="item item--right" style="right:53px;top:369px;width:170px;">
      <div class="item-name"><span class="price" style="position:absolute;left:21px;">14.80</span>Kuy Teav Char</div>
      <div class="item-desc">Stir-fired rice noodles, minced pork, ham, egg, bea<br>sprouts and peanut sauce</div>
    </div>
    <div class="item item--right" style="right:53px;top:405px;width:170px;">
      <div class="item-name"><span class="price" style="position:absolute;left:17px;">16.50</span>Lemongrass Fried Rice</div>
      <div class="item-desc">Lemongrass, onion, chicken or beef carrot and French beans</div>
    </div>
  </section>

  <!-- Mains and grill -->
  <section class="page page--mains">
    <div class="artwork artwork--top-right" role="img" aria-label="Watercolour peach and pink roses with teal leaves"></div>
    <div class="artwork artwork--bottom-left" role="img" aria-label="Watercolour pink roses with teal leaves"></div>
    <svg class="frame" viewBox="0 0 342 484" aria-hidden="true">
      <path d="M207 20 H20 V167"/><path d="M207 25 H25 V167"/>
      <path d="M173 465 H323 V279"/><path d="M173 460 H318 V279"/>
    </svg>

    <div class="section-label" style="left:42px;top:68px;width:89px;">LOTUVAN DISH</div>

    <div class="item" style="left:48px;top:97px;">
      <div class="item-name">Fish Amok &nbsp;&nbsp;27.00</div>
      <div class="item-desc">"Traditional Cambodian Dish in a banana leaf,<br>Markel fish, curry paste, coconut, Chinese Broccoli served with Jasmine rice"</div>
    </div>
    <div class="item" style="left:48px;top:128px;">
      <div class="item-name">Red Curry 17.00</div>
      <div class="item-desc">Red Curry with chicken &amp; vegetable</div>
    </div>
    <div class="item" style="left:48px;top:151px;">
      <div class="item-name">Green Curry 17.00</div>
      <div class="item-desc">Green Curry with Beef or Fish (Markel filet), with pineapple, eggplant &amp; bamboo</div>
    </div>
    <div class="item" style="left:48px;top:181px;">
      <div class="item-name">Kampot Pepper with Seafood &nbsp;&nbsp;25.00</div>
      <div class="item-desc">Kampot Pepper with Seafood, onion, carrot &amp; dust of Spring onion</div>
    </div>
    <div class="item" style="left:48px;top:203px;">
      <div class="item-name">Char Kreung Chicken or Fish &nbsp;&nbsp;22.00</div>
      <div class="item-desc">Stirred-fried of commination chicken or fish, mix vegetable, green beans, sweet chilli</div>
    </div>
    <div class="item" style="left:48px;top:226px;">
      <div class="item-name">Beef Loc Lac24.50</div>
      <div class="item-desc">Cambodian marinated beef chunks and vegetable served with crispy sweet potato strips</div>
    </div>
    <div class="item" style="left:48px;top:249px;">
      <div class="item-name">Traditional Lotuvan Soup &nbsp;21.00</div>
      <div class="item-desc">A mild spicy sweet and &nbsp;sour soup with fish &amp; mushrooms</div>
    </div>

    <div class="section-label section-label--right" style="left:258px;top:284px;width:58px;">Grill</div>

    <div class="item item--right" style="right:47px;top:308px;width:220px;">
      <div class="item-name">14.50 &nbsp;&nbsp;Beef Skewers with Papaya Salad</div>
      <div class="item-desc">Beef Skewers (4 pcs) with Papaya Salad served with a slice of baguette</div>
    </div>
    <div class="item item--right" style="right:47px;top:330px;width:220px;">
      <div class="item-name">17.00 &nbsp;&nbsp;&nbsp;&nbsp;&nbsp;My Grandmothers Dish</div>
      <div class="item-desc">Grilled chicken tights with brown rice and tomato salad</div>
    </div>
    <div class="item item--right" style="right:47px;top:353px;width:220px;">
      <div class="item-name">8.00 &nbsp;&nbsp;Grilled Corn Cob</div>
      <div class="item-desc">Grilled corn with coconut glaze and spring onion (2 per serve)</div>
    </div>
    <div class="item item--right" style="right:47px;top:375px;width:220px;">
      <div class="item-name">25.00 &nbsp;&nbsp;&nbsp;Old School Spareribs</div>
      <div class="item-desc">Grilled pork rib with mixed spices and served with carrot salad</div>
    </div>
    <div class="item item--right" style="right:47px;top:398px;width:220px;">
      <div class="item-name">26.00 &nbsp;&nbsp;&nbsp;Grilled Pork Neck</div>
      <div class="item-desc">Grilled Pork Neck with tamarin sauce, mixed salad and jasmine rice</div>
    </div>
  </section>

  <!-- Salads, desserts, sides -->
  <section class="page page--tall page--salads">
    <div class="artwork artwork--top-right" role="img" aria-label="Watercolour peach and pink roses with teal leaves"></div>
    <div class="artwork artwork--bottom-left" role="img" aria-label="Watercolour pink roses with teal leaves"></div>
    <svg class="frame" viewBox="0 0 342 488" aria-hidden="true">
      <path d="M207 20 H20 V167"/><path d="M207 25 H25 V167"/>
      <path d="M173 469 H323 V283"/><path d="M173 464 H318 V283"/>
    </svg>

    <div class="section-label" style="left:39px;top:44px;width:89px;">Salads</div>

    <div class="item" style="left:49px;top:71px;">
      <div class="item-name">Glass Noodle Salad &nbsp;20.00</div>
      <div class="item-desc" style="font-size:7px;line-height:10px;margin-top:3px;">With Chicken or Pork</div>
    </div>
    <div class="item" style="left:49px;top:105px;">
      <div class="item-name">Beef Salad &nbsp;&nbsp;&nbsp;22.00</div>
      <div class="item-desc" style="font-size:7px;line-height:10px;margin-top:2px;">With home made dressing &amp; herbs</div>
    </div>
    <div class="item" style="left:49px;top:137px;">
      <div class="item-name">Tofu Salad &nbsp;&nbsp;&nbsp;&nbsp;19.50</div>
      <div class="item-desc" style="font-size:7px;line-height:10px;margin-top:2px;">Mixed Asian salad with herbs &amp; coconut dressing.</div>
    </div>

    <div class="section-label section-label--center" style="left:112px;top:192px;width:90px;">Desert:</div>

    <div class="item item--center" style="left:58px;top:218px;width:200px;">
      <div class="item-name">Yellow Bean with Glutenous Rice) &nbsp;&nbsp;&nbsp;8.50</div>
      <div class="item-desc" style="font-size:6.6px;line-height:9px;">With coconut and caramel (2 pcs</div>
    </div>
    <div class="item item--center" style="left:58px;top:243px;width:200px;">
      <div class="item-name">Black Rice Pudding &nbsp;8.50</div>
      <div class="item-desc" style="font-size:6.6px;line-height:9px;">With yellow bean and a drop of coconut cream</div>
    </div>
    <div class="item item--center" style="left:58px;top:267px;width:200px;">
      <div class="item-name">Pumpkin Custard &nbsp;&nbsp;&nbsp;&nbsp;9.00</div>
      <div class="item-desc" style="font-size:6.6px;line-height:9px;">Soft pumpkin custard filled sweet coconut cream</div>
    </div>

    <div class="section-label section-label--center" style="left:208px;top:316px;width:90px;">SIDE &nbsp;DISH</div>

    <div class="item item--right" style="right:57px;top:350px;"><div class="item-name">03.00 &nbsp;&nbsp;Steamed Jasmine Rice</div></div>
    <div class="item item--right" style="right:57px;top:368px;"><div class="item-name">05.00 &nbsp;&nbsp;&nbsp;Steamed Vegetable</div></div>
    <div class="item item--right" style="right:57px;top:385px;"><div class="item-name">04.00 &nbsp;&nbsp;&nbsp;&nbsp;Steamed Noodle</div></div>
    <div class="item item--right" style="right:57px;top:403px;"><div class="item-name">05.50 &nbsp;&nbsp;&nbsp;&nbsp;&nbsp;&nbsp;&nbsp;&nbsp;&nbsp;Rice Peanut</div></div>
    <div class="item item--right" style="right:57px;top:421px;"><div class="item-name">04.00 &nbsp;&nbsp;&nbsp;&nbsp;&nbsp;&nbsp;&nbsp;Peanut Sauce</div></div>
  </section>

  <!-- Notes and dietary key -->
  <section class="page page--tall page--notes">
    <div class="artwork artwork--top-left" role="img" aria-label="Watercolour pink roses, lilac flowers and coral feathers"></div>
    <div class="artwork artwork--bottom-right" role="img" aria-label="Watercolour roses, lilac flowers and coral feathers"></div>

    <ul class="notes-list">
      <li>10% Surchge On Public Holiday.</li>
      <li>All Price Are Include Holiday.</li>
      <li>All Price Are Subject To Be Change Withouy Prior Notice.</li>
      <li>If You Are Concerned With Allergies To Certain Ingredients Please Inform Our Staff.</li>
      <li>Food Ingridents And Prices Are Subject To Be Changed Without Prior Notic.</li>
    </ul>

    <span class="dietary-key" style="left:47px;top:280px;">VEGETARIAN</span>
    <span class="dietary-key" style="left:147px;top:280px;">VEGAN</span>
    <span class="dietary-key" style="left:218px;top:280px;">GLUTEN &nbsp;FREE</span>
    <span class="dietary-key" style="left:71px;top:298px;">RATE &nbsp;OF &nbsp;SPICE</span>
    <span class="dietary-key" style="left:173px;top:298px;">CONTAIN &nbsp;PEANUT</span>
  </section>

</main>
</body>
</html>
```